I have a basketball training business combined with a strength training business. I train professio

I recently saw the cats that won the contest in the strength coach business card competition. I loved the design. I.want a card with my logo that calls attention to my clients as the card that won did to me. I would like to see if I could get a similar design. My logo is what I like although I must say I like the red and black design of the contest winner. perhaps if the smaller lettered portion of my logo coukd be separated from the larger KRT logo. It almost looks like 3M3. I like.the KRT Training and Development portion of it. I need help.

Training

```html
<!DOCTYPE html>
<html lang="en">
<head>
<meta charset="UTF-8">
<title>KRT Training and Development – Business Card</title>
<link href="https://fonts.googleapis.com/css2?family=Lato:wght@400;700;900&display=swap" rel="stylesheet">
<style>
  :root {
    --ink: #2f2f2f;
    --red: #e3242b;
    --paper: #ffffff;
    --page: #ffffff;
  }
  * { margin: 0; padding: 0; box-sizing: border-box; }
  html, body {
    width: 1200px;
    height: 1000px;
    overflow: hidden;
    background: var(--page);
    font-family: "Lato", sans-serif;
  }
  .business-card {
    position: absolute;
    left: 170px;
    top: 253px;
    width: 860px;
    height: 494px;
    background: var(--paper);
    box-shadow: 5px 6px 8px rgba(0,0,0,0.35);
    border: 1px solid #ececec;
  }
  .brand-name {
    position: absolute;
    top: 18px;
    left: 0;
    width: 100%;
    text-align: center;
    font-weight: 900;
    font-size: 64px;
    line-height: 1;
    letter-spacing: 4px;
    color: var(--ink);
  }
  .brand-tagline {
    position: absolute;
    top: 114px;
    left: 0;
    width: 100%;
    text-align: center;
    font-weight: 900;
    font-size: 28px;
    line-height: 1;
    text-transform: uppercase;
    color: var(--ink);
  }
  .divider {
    position: absolute;
    left: 50%;
    height: 2px;
    background: var(--red);
    transform: translateX(-50%);
  }
  .divider--long { top: 184px; width: 675px; }
  .divider--short { top: 320px; width: 365px; }
  .coach-name {
    position: absolute;
    top: 214px;
    left: 0;
    width: 100%;
    text-align: center;
    font-weight: 700;
    font-size: 46px;
    line-height: 1;
    letter-spacing: 8px;
    color: var(--red);
  }
  .coach-title {
    position: absolute;
    top: 264px;
    left: 0;
    width: 100%;
    text-align: center;
    font-weight: 700;
    font-size: 22px;
    line-height: 1;
    color: var(--ink);
  }
  .phone-icon {
    position: absolute;
    top: 356px;
    left: 50%;
    transform: translateX(-50%);
  }
  .phone-number {
    position: absolute;
    top: 390px;
    left: 0;
    width: 100%;
    text-align: center;
    font-weight: 700;
    font-size: 28px;
    line-height: 1;
    color: var(--ink);
  }
  .website {
    position: absolute;
    top: 448px;
    left: 0;
    width: 100%;
    text-align: center;
    font-weight: 400;
    font-size: 27px;
    line-height: 1;
    color: var(--ink);
  }
  .website .accent { color: var(--red); }
</style>
</head>
<body>
  <div class="business-card">
    <div class="brand-name">KRT</div>
    <div class="brand-tagline">KRT Training and Development</div>
    <div class="divider divider--long"></div>
    <div class="coach-name">RICKY DALTON</div>
    <div class="coach-title">CERTIFIED FUNCTIONAL STRENGHT COACH</div>
    <div class="divider divider--short"></div>
    <svg class="phone-icon" width="40" height="28" viewBox="0 0 40 28" aria-label="Phone">
      <rect x="14" y="2" width="12" height="23" rx="2" fill="none" stroke="var(--red)" stroke-width="2.2"/>
      <line x1="18" y1="21" x2="22" y2="21" stroke="var(--red)" stroke-width="2"/>
      <path d="M9 8 Q6 13.5 9 19" fill="none" stroke="var(--red)" stroke-width="2" stroke-linecap="round"/>
      <path d="M4 5 Q-0.5 13.5 4 22" fill="none" stroke="var(--red)" stroke-width="2" stroke-linecap="round"/>
      <path d="M31 8 Q34 13.5 31 19" fill="none" stroke="var(--red)" stroke-width="2" stroke-linecap="round"/>
      <path d="M36 5 Q40.5 13.5 36 22" fill="none" stroke="var(--red)" stroke-width="2" stroke-linecap="round"/>
    </svg>
    <div class="phone-number">555-013-0427</div>
    <div class="website"><span class="accent">ricky</span>dalton<span class="accent">hoops</span>.com</div>
  </div>
</body>
</html>
```